Naturopath Practitioner Card Design

I am a naturopath needing a design for a business card mainly to show that I am a naturopath and have some contact details to give to prospective clients. I am open minded about the design and what is on the second side of the card whether it just be some artwork or space for details, appointment times etc. Naturopathy is the practice of natural medicine that uses a holistic approach and incorporates herbal and nutritional medicine.

Contact Information for Business Card

Tom Waverly NaturopathBHSc (Naturopathy) Member NHPG 0491 582 736 tom.waverly@mailbox-example.net www.tomwaverlynaturopathy.example.au

Requirements
Nice to have
• Would prefer some kind of original pattern/art work/logo rather than an image, not fussed if its very simple/basic
• I am open to any colour but think I would prefer a more earthy sandy clay etc type style than the greens that are commonly associated with naturopathy.
Should not have
• Don't really want to have generic stock images on it

```html
<!DOCTYPE html>
<html lang="en">
<head>
<meta charset="utf-8">
<title>Tom Waverly – Naturopath Business Card</title>
<link rel="stylesheet" href="https://fonts.googleapis.com/css2?family=Open+Sans:ital,wght@0,400;0,600;0,700;1,700&display=swap">
<style>
  :root {
    --page-bg: #d9d9d7;
    --green-light: #7ce512;
    --green-mid: #3fa81c;
    --green-deep: #0c6b1f;
    --vine-green: #0a7a1c;
    --card-white: #ffffff;
    --title-green: #3f9a2a;
    --label-ink: #222222;
    --rule-green: #8cc48a;
    --rule-green-strong: #3f9a2a;
    --notice-navy: #1d2b4a;
    --vine-grey: #e3e7e3;
    --text-light: #ffffff;
  }
  * { box-sizing: border-box; margin: 0; padding: 0; }
  html, body {
    width: 1200px;
    height: 900px;
    overflow: hidden;
  }
  body {
    background: var(--page-bg);
    font-family: "Open Sans", Arial, sans-serif;
    display: flex;
    flex-direction: column;
    align-items: center;
    justify-content: center;
    gap: 36px;
  }
  .card {
    position: relative;
    width: 660px;
    height: 400px;
    overflow: hidden;
    box-shadow: 0 6px 18px rgba(0, 0, 0, 0.18);
  }

  /* Front side */
  .card-front {
    background: linear-gradient(180deg, var(--green-light) 0%, var(--green-mid) 55%, var(--green-deep) 100%);
    color: var(--text-light);
  }
  .front-vine {
    position: absolute;
    right: 0;
    bottom: 0;
    width: 330px;
    height: 330px;
    border-top-left-radius: 100% 100%;
    background: radial-gradient(circle at 85% 85%, rgba(10, 122, 28, 0.55), rgba(10, 122, 28, 0) 70%);
  }
  .identity {
    position: absolute;
    left: 58px;
    top: 56px;
  }
  .practitioner-name {
    font-size: 26px;
    font-weight: 700;
    margin-bottom: 10px;
  }
  .practitioner-role,
  .practitioner-credentials {
    font-size: 19px;
    font-weight: 400;
    line-height: 1.55;
  }
  .contact-list {
    position: absolute;
    left: 58px;
    top: 214px;
    list-style: none;
  }
  .contact-item {
    display: flex;
    align-items: center;
    gap: 12px;
    font-size: 18px;
    line-height: 1.6;
  }
  .contact-icon {
    width: 14px;
    height: 14px;
    flex: none;
  }

  /* Back side */
  .card-back {
    background: var(--card-white);
  }
  .back-vine {
    position: absolute;
    right: 0;
    bottom: 0;
    width: 300px;
    height: 330px;
    border-top-left-radius: 100% 100%;
    background: radial-gradient(circle at 80% 70%, var(--vine-grey), rgba(227, 231, 227, 0) 70%);
  }
  .appointment-title {
    position: absolute;
    top: 44px;
    left: 0;
    right: 0;
    text-align: center;
    color: var(--title-green);
    font-size: 26px;
    font-weight: 700;
  }
  .appointment-fields {
    position: absolute;
    left: 60px;
    right: 60px;
    top: 108px;
  }
  .field-row {
    display: flex;
    align-items: flex-end;
    height: 42px;
    font-size: 16px;
    color: var(--label-ink);
  }
  .field-label {
    width: 64px;
    flex: none;
  }
  .field-line {
    flex: 1;
    border-bottom: 1px solid var(--rule-green);
    margin-bottom: 5px;
  }
  .field-time .field-line {
    border-bottom-color: var(--rule-green-strong);
  }
  .meridiem {
    padding: 0 16px 0 12px;
  }
  .meridiem:last-child {
    padding-right: 0;
  }
  .cancellation-notice {
    position: absolute;
    left: 0;
    right: 0;
    top: 270px;
    text-align: center;
    color: var(--notice-navy);
    font-size: 16px;
    font-weight: 700;
    font-style: italic;
  }
</style>
</head>
<body>

  <section class="card card-front" aria-label="Business card front">
    <div class="front-vine" role="img" aria-label="Curling green vine ornament"></div>
    <div class="identity">
      <h1 class="practitioner-name">Tom Waverly</h1>
      <p class="practitioner-role">Naturopath</p>
      <p class="practitioner-credentials">BHSc (Naturopathy) Member NHPG</p>
    </div>
    <ul class="contact-list">
      <li class="contact-item">
        <svg class="contact-icon" viewBox="0 0 16 16" aria-hidden="true">
          <path fill="#ffffff" d="M3.2 1.2l2.3 2.6-1.2 1.7c.9 2 2.3 3.4 4.2 4.3l1.7-1.2 2.6 2.3-1.3 2.3C6.6 13.2 2.8 9.4 1 4.5z"/>
        </svg>
        <span>0491 582 736</span>
      </li>
      <li class="contact-item">
        <svg class="contact-icon" viewBox="0 0 16 16" aria-hidden="true">
          <rect x="1" y="3" width="14" height="10" fill="#ffffff"/>
          <path d="M1.5 3.5L8 8.5l6.5-5" fill="none" stroke="#3fa81c" stroke-width="1.3"/>
        </svg>
        <span>tom.waverly@mailbox-example.net</span>
      </li>
    </ul>
  </section>

  <section class="card card-back" aria-label="Business card back">
    <div class="back-vine" role="img" aria-label="Faint grey vine ornament"></div>
    <h2 class="appointment-title">Your Next Appointment is</h2>
    <div class="appointment-fields">
      <div class="field-row"><span class="field-label">Name :</span><span class="field-line"></span></div>
      <div class="field-row"><span class="field-label">Date :</span><span class="field-line"></span></div>
      <div class="field-row field-time">
        <span class="field-label">Time:</span>
        <span class="field-line"></span><span class="meridiem">AM</span>
        <span class="field-line"></span><span class="meridiem">PM</span>
      </div>
    </div>
    <p class="cancellation-notice">If unable to keep appointment, kindly give 24hrs notice.</p>
  </section>

</body>
</html>
```